Jewelry Website needs fully functional Website (Wordpress + Ecommerce))

The Wordpress site will have to be fully functional with an Ecommerce integration and will need to be SEO optimized.
We would like to have an Instagram integration to the website so viewers can see updates posted (see larkfenwick.ca)
We sell real fine gold and diamond jewelry. The website should have an elegant, modern, professional and high end look. It will be the decision maker for people to order their jewelry from the website, therefore it should be easily navigated by users.
Target Audience are women from 16-50 years old.
Attached is a Logo of our brand that will command how the website should look.
For inspiration purposes here is a list of websites that we like:
larkfenwick.ca/
http://www.coralvinta.com/
Get creative and show us your talent!
Target Market(s)
The target market are women ages 16-50.
Industry/Entity Type
Jewelry
Look and feel

```html
<!DOCTYPE html>
<html lang="en">
<head>
<meta charset="utf-8">
<title>Celina M Jewellery</title>
<link rel="stylesheet" href="https://fonts.googleapis.com/css2?family=Bodoni+Moda:wght@500&family=Libre+Baskerville:ital,wght@0,400;1,400&family=Raleway:wght@200;300&display=swap">
<style>
  :root {
    --ink: #111111;
    --black: #000000;
    --white: #ffffff;
    --muted: #8a8a8a;
    --rule: #d9d9d9;
    --gold: #e8c300;
    --nav-grey: #b8b8b8;
  }
  * { box-sizing: border-box; margin: 0; padding: 0; }
  html, body { width: 932px; height: 1200px; overflow: hidden; background: var(--white); }
  body { position: relative; font-family: "Libre Baskerville", Georgia, serif; color: var(--ink); }

  .hero { position: absolute; left: 0; top: 0; width: 932px; height: 552px; background: var(--black); overflow: hidden; }
  .hero-photo { position: absolute; left: 280px; top: 0; width: 652px; height: 552px;
    background:
      radial-gradient(ellipse 260px 300px at 330px 260px, #8e8e8e 0%, #5a5a5a 45%, rgba(30,30,30,0) 100%),
      radial-gradient(ellipse 200px 260px at 560px 180px, #9a9a9a 0%, rgba(40,40,40,0) 100%),
      linear-gradient(90deg, #000 0%, #1a1a1a 25%, #3a3a3a 100%); }

  .site-header { position: absolute; left: 129px; top: 12px; width: 673px; height: 50px; }
  .brand { position: absolute; left: 0; top: 0; display: flex; align-items: center; gap: 12px; color: var(--white); }
  .brand-ring { width: 48px; height: 48px; border: 1.5px solid var(--white); border-radius: 50%; }
  .brand-name { font-size: 18px; letter-spacing: 1px; white-space: nowrap; }
  .main-nav { position: absolute; left: 233px; top: 23px; width: 407px; display: flex; justify-content: space-between;
    font-size: 7.6px; letter-spacing: 0.3px; color: var(--nav-grey); white-space: nowrap; }
  .main-nav span { white-space: nowrap; }
  .main-nav .is-current { color: var(--white); }
  .cart { position: absolute; left: 660px; top: 17px; }

  .hero-copy { position: absolute; left: 132px; top: 226px; }
  .hero-kicker { font-family: "Raleway", sans-serif; font-weight: 200; font-size: 36px; color: #d0d0d0; letter-spacing: 1px; line-height: 1; }
  .hero-title { font-family: "Bodoni Moda", serif; font-weight: 500; font-size: 49px; color: var(--white); letter-spacing: 2px; line-height: 1; margin-top: 16px; white-space: nowrap; }
  .hero-sub { font-family: "Raleway", sans-serif; font-weight: 300; font-size: 13.6px; color: #d0d0d0; letter-spacing: 0.6px; margin-top: 17px; white-space: nowrap; }
  .hero-sub .accent { color: var(--gold); }

  .category { position: absolute; top: 568px; width: 330px; height: 265px; }
  .category.diamond { left: 130px; }
  .category.gold { left: 477px; }
  .category-photo { position: absolute; left: 23px; top: 22px; width: 303px; height: 242px;
    clip-path: polygon(73px 0, 100% 0, 100% 100%, 0 100%, 0 73px); }
  .diamond .category-photo { background: radial-gradient(ellipse 120px 140px at 190px 110px, #d8b7a6 0%, #9c7a6c 40%, #1b222a 100%); }
  .gold .category-photo { background: radial-gradient(ellipse 130px 150px at 220px 120px, #a5623a 0%, #6f5545 45%, #5a5a55 100%); }
  .category-line { position: absolute; left: 0; top: 0; }
  .category-label { position: absolute; font-size: 16px; letter-spacing: 1.5px; color: #222; transform: rotate(-45deg); transform-origin: left bottom; white-space: nowrap; }
  .diamond .category-label { left: 14px; top: 72px; }
  .gold .category-label { left: 32px; top: 52px; }

  .instagram-title { position: absolute; left: 129px; top: 874px; font-size: 18px; letter-spacing: 1px; color: #111; font-weight: 400; }
  .insta-grid { position: absolute; left: 129px; top: 916px; display: flex; gap: 12px; }
  .insta-tile { width: 125px; height: 125px; }
  .t1 { background: linear-gradient(160deg, #e8d6bf, #c9a37a 60%, #b88a5a); }
  .t2 { background: linear-gradient(160deg, #8a5440, #2a2226 55%, #9c6a4c); }
  .t3 { background: linear-gradient(160deg, #d9b48f, #f2f2f2 55%, #e9e9e9); }
  .t4 { background: linear-gradient(160deg, #3a2a28, #c99a86 50%, #b0242a); }
  .t5 { background: linear-gradient(160deg, #6b6660, #d3b8a0 50%, #55514c); }

  .footer-rule { position: absolute; left: 0; top: 1090px; width: 932px; height: 1px; background: var(--rule); }
  .footer-links { position: absolute; left: 131px; top: 1110px; display: flex; font-size: 8.2px; letter-spacing: 0.5px; color: var(--muted); white-space: nowrap; }
  .footer-links li { list-style: none; padding: 0 8px; border-left: 1px solid var(--rule); }
  .footer-links li:first-child { padding-left: 0; border-left: 0; color: #111; }
  .newsletter { position: absolute; left: 621px; top: 1103px; width: 181px; height: 24px; border: 1px solid #333; display: flex; }
  .newsletter-field { flex: 1; font-size: 7.6px; font-style: italic; color: var(--muted); padding: 7px 0 0 7px; }
  .newsletter-send { width: 27px; background: var(--black); display: flex; align-items: center; justify-content: center; }

  .site-bottom { position: absolute; left: 0; top: 1146px; width: 932px; height: 54px; background: var(--black); }
  .social { position: absolute; left: 129px; top: 18px; display: flex; gap: 9px; }
  .social span { width: 18px; height: 18px; background: #d8d8d8; display: block; }
  .social span:first-child { background: #2aa3ef; }
  .bottom-brand { position: absolute; left: 448px; top: 12px; }
  .bottom-brand .ring { display: block; width: 30px; height: 30px; border: 1.5px solid var(--white); border-radius: 50%; }
  .copyright { position: absolute; right: 130px; top: 22px; font-size: 6.8px; color: #9a9a9a; letter-spacing: 0.2px; white-space: nowrap; }
  .copyright strong { color: var(--white); font-weight: 400; }
</style>
</head>
<body>
  <section class="hero">
    <div class="hero-photo" role="img" aria-label="Black and white portrait of a model with flowing hair wearing a diamond and amethyst necklace and earrings"></div>

    <header class="site-header">
      <div class="brand"><span class="brand-ring"></span><span class="brand-name">Celina M</span></div>
      <nav class="main-nav">
        <span class="is-current">HOME</span><span>ABOUT</span><span>DIAMOND JEWELLERY</span><span>GOLD JEWELLERY</span><span>WHATS NEW</span><span>CONTACT</span>
      </nav>
      <svg class="cart" width="15" height="16" viewBox="0 0 15 16" aria-label="Shopping bag">
        <path d="M1.5 5h12l-1 10h-10z" fill="none" stroke="#fff" stroke-width="1.2"/>
        <path d="M4.5 6V3.5a3 3 0 0 1 6 0V6" fill="none" stroke="#fff" stroke-width="1.2"/>
      </svg>
    </header>

    <div class="hero-copy">
      <p class="hero-kicker">FASHION</p>
      <h1 class="hero-title">CELINA M</h1>
      <p class="hero-sub">DIAMOND JEWELLERY &amp; <span class="accent">GOLD JEWELLERY</span></p>
    </div>
  </section>

  <section class="category diamond">
    <div class="category-photo" role="img" aria-label="Model wearing a diamond necklace, earrings and bracelet against a dark background"></div>
    <svg class="category-line" width="120" height="120" viewBox="0 0 120 120"><line x1="0" y1="118" x2="118" y2="0" stroke="#111" stroke-width="1"/></svg>
    <span class="category-label">DIAMOND</span>
  </section>

  <section class="category gold">
    <div class="category-photo" role="img" aria-label="Model in a gold headdress wearing gold earrings and stacked gold bangles"></div>
    <svg class="category-line" width="120" height="120" viewBox="0 0 120 120"><line x1="0" y1="118" x2="118" y2="0" stroke="#111" stroke-width="1"/></svg>
    <span class="category-label">GOLD</span>
  </section>

  <h2 class="instagram-title">INSTAGRAM</h2>
  <div class="insta-grid">
    <div class="insta-tile t1" role="img" aria-label="Ornate gold bridal necklace and earrings"></div>
    <div class="insta-tile t2" role="img" aria-label="Silver back necklace on a dark dress"></div>
    <div class="insta-tile t3" role="img" aria-label="Layered fine gold necklaces over a white top"></div>
    <div class="insta-tile t4" role="img" aria-label="Diamond collar necklace and cocktail ring"></div>
    <div class="insta-tile t5" role="img" aria-label="Model wearing gold bangles and a gold pendant"></div>
  </div>

  <div class="footer-rule"></div>
  <ul class="footer-links">
    <li>ABOUT US</li><li>CUSTOMER SERVICE</li><li>PRIVACY POLICY</li><li>SITE MAP</li><li>CONTACT US</li>
  </ul>
  <form class="newsletter">
    <span class="newsletter-field">@your email...</span>
    <span class="newsletter-send">
      <svg width="12" height="11" viewBox="0 0 12 11"><path d="M0 5l12-5-3 11-3-4-3 2 1-3 5-5-6 4z" fill="#fff"/></svg>
    </span>
  </form>

  <footer class="site-bottom">
    <div class="social" aria-label="Social links"><span></span><span></span><span></span><span></span><span></span><span></span><span></span></div>
    <div class="bottom-brand"><span class="ring"></span></div>
    <p class="copyright">© 2014 - 2015 <strong>CELINA M JEWELLERY.</strong> ALL RIGHTS RESERVED.</p>
  </footer>
</body>
</html>
```